Daycare Letterhead and Business Card

Looking for a modern, playful and happy letterhead and business card design for a home childcare / daycare franchise concept where it can be easily customized to the specific locations name ( Mabel's Home Daycare or Rosa's Daycare etc ).

Logo concept can be open - possibly a giraffe or child illustration.

Letterhead must be in Word must be EASILY edible in Word for non-technical person. The design of the header and footer should leave as much room as possible on page for content.

Ideally the business card should be in Word as well but can be in Photoshop as well.

Samples of what we are looking for in colors and design
https://plinkomart.net/item/bright-class-advert-leaflets/7281930
https://plinkomart.net/item/office-leaflet-tots-cheer/8392016
https://plinkomart.net/item/class-leaflet/26810482

```html
<!DOCTYPE html>
<html lang="en">
<head>
<meta charset="utf-8">
<title>Mabel's Home Daycare – Business Card</title>
<link rel="stylesheet" href="https://fonts.googleapis.com/css2?family=Dancing+Script:wght@600&family=Open+Sans:wght@400;600;700&display=swap">
<style>
  :root {
    --bg: #e9ecee;
    --white: #ffffff;
    --orange: #f7901e;
    --blue: #29abe2;
    --yellow: #ffed00;
    --red: #ed1c24;
    --cloud: #d0d0d0;
    --ink: #222222;
    --logo: #1b75bc;
  }
  * { box-sizing: border-box; margin: 0; padding: 0; }
  html, body { width: 1200px; height: 900px; overflow: hidden; }
  body {
    background: var(--bg);
    font-family: "Open Sans", Arial, sans-serif;
    display: flex;
    align-items: center;
    justify-content: center;
    gap: 80px;
  }
  .card {
    position: relative;
    width: 360px;
    height: 580px;
    border-radius: 18px;
    background: var(--white);
    overflow: hidden;
    box-shadow: 0 6px 18px rgba(0,0,0,0.15);
  }
  .card-art { position: absolute; inset: 0; width: 100%; height: 100%; }

  .brand {
    position: absolute;
    display: flex;
    align-items: center;
    gap: 8px;
    font-weight: 700;
    color: var(--logo);
    white-space: nowrap;
  }
  .brand-dot { width: 14px; height: 14px; border-radius: 50%; background: var(--orange); flex: none; }

  /* contact side */
  .holder { position: absolute; left: 34px; top: 64px; }
  .holder-name {
    font-family: "Dancing Script", cursive;
    font-size: 36px;
    color: var(--logo);
    line-height: 1;
  }
  .holder-title { font-size: 16px; color: var(--ink); margin-top: 6px; }

  .front .brand { left: 40px; top: 300px; font-size: 18px; }

  .contacts { position: absolute; left: 40px; top: 350px; list-style: none; }
  .contacts li {
    display: flex; align-items: center; gap: 10px;
    font-size: 16px; color: var(--ink); line-height: 32px;
  }
  .contacts svg { width: 20px; height: 20px; flex: none; }

  /* logo side */
  .back .brand {
    left: 50%; top: 50%; transform: translate(-50%, -50%);
    font-size: 22px;
  }
</style>
</head>
<body>

<!-- Contact side -->
<section class="card front">
  <svg class="card-art" viewBox="0 0 360 580" aria-hidden="true">
    <defs><clipPath id="front-clip"><rect width="360" height="580" rx="18"/></clipPath></defs>
    <g clip-path="url(#front-clip)">
      <circle cx="180" cy="-250" r="486" fill="var(--red)"/>
      <circle cx="180" cy="-250" r="472" fill="var(--yellow)"/>
      <circle cx="180" cy="-250" r="458" fill="var(--blue)"/>
      <circle cx="180" cy="-250" r="444" fill="var(--white)"/>
      <circle cx="180" cy="-250" r="438" fill="var(--orange)"/>
      <!-- slashes -->
      <g stroke="var(--blue)" stroke-width="2" stroke-linecap="round">
        <line x1="40" y1="262" x2="82" y2="240"/>
        <line x1="44" y1="272" x2="92" y2="246"/>
        <line x1="52" y1="280" x2="88" y2="260"/>
      </g>
      <!-- corner triangle -->
      <path d="M360 490 L360 580 L270 580 Z" fill="var(--blue)"/>
      <path d="M360 490 L270 580 L290 490 Z" fill="var(--orange)"/>
      <!-- edge bands -->
      <rect x="0" y="0" width="8" height="290" fill="var(--red)"/>
      <rect x="0" y="290" width="8" height="290" fill="var(--yellow)"/>
      <rect x="352" y="0" width="8" height="290" fill="var(--yellow)"/>
      <rect x="352" y="290" width="8" height="290" fill="var(--orange)"/>
      <rect x="0" y="572" width="120" height="8" fill="var(--yellow)"/>
      <rect x="120" y="572" width="120" height="8" fill="var(--blue)"/>
      <rect x="240" y="572" width="120" height="8" fill="var(--orange)"/>
    </g>
  </svg>

  <div class="holder">
    <p class="holder-name">Nora Vell</p>
    <p class="holder-title">Chief Director</p>
  </div>

  <div class="brand"><span class="brand-dot"></span>Mabel's Home Daycare</div>

  <ul class="contacts">
    <li>
      <svg viewBox="0 0 18 18"><circle cx="9" cy="9" r="9" fill="var(--blue)"/><path d="M9 4a3 3 0 0 0-3 3c0 2.3 3 6 3 6s3-3.7 3-6a3 3 0 0 0-3-3zm0 4.2a1.2 1.2 0 1 1 0-2.4 1.2 1.2 0 0 1 0 2.4z" fill="#fff"/></svg>
      Street Address Here
    </li>
    <li>
      <svg viewBox="0 0 18 18"><circle cx="9" cy="9" r="9" fill="var(--blue)"/><path d="M6.2 4.5l1.6 1.9-.9 1.2c.6 1.3 1.4 2.1 2.6 2.7l1.2-.9 1.9 1.6-.8 1.6c-3.4-.3-6.1-3-6.4-6.4z" fill="#fff"/></svg>
      +000 1234 567890
    </li>
    <li>
      <svg viewBox="0 0 18 18"><circle cx="9" cy="9" r="9" fill="var(--blue)"/><circle cx="9" cy="9" r="4.5" fill="none" stroke="#fff" stroke-width="1.2"/><line x1="4.5" y1="9" x2="13.5" y2="9" stroke="#fff" stroke-width="1.2"/><ellipse cx="9" cy="9" rx="2" ry="4.5" fill="none" stroke="#fff" stroke-width="1.2"/></svg>
      urwebsitename.com
    </li>
    <li>
      <svg viewBox="0 0 18 18"><circle cx="9" cy="9" r="9" fill="var(--blue)"/><rect x="4.5" y="6" width="9" height="6.5" rx="1" fill="none" stroke="#fff" stroke-width="1.2"/><path d="M4.8 6.4L9 9.6l4.2-3.2" fill="none" stroke="#fff" stroke-width="1.2"/></svg>
      urname@mailbox.com
    </li>
  </ul>
</section>

<!-- Logo side -->
<section class="card back">
  <svg class="card-art" viewBox="0 0 360 580" aria-hidden="true">
    <defs><clipPath id="back-clip"><rect width="360" height="580" rx="18"/></clipPath></defs>
    <g clip-path="url(#back-clip)">
      <g fill="var(--cloud)">
        <circle cx="120" cy="230" r="80"/>
        <circle cx="230" cy="210" r="85"/>
        <circle cx="255" cy="320" r="80"/>
        <circle cx="170" cy="380" r="80"/>
        <circle cx="95" cy="330" r="70"/>
        <circle cx="180" cy="290" r="90"/>
      </g>
      <rect x="0" y="0" width="120" height="8" fill="var(--red)"/>
      <rect x="120" y="0" width="120" height="8" fill="var(--blue)"/>
      <rect x="240" y="0" width="120" height="8" fill="var(--yellow)"/>
      <rect x="0" y="572" width="120" height="8" fill="var(--yellow)"/>
      <rect x="120" y="572" width="120" height="8" fill="var(--blue)"/>
      <rect x="240" y="572" width="120" height="8" fill="var(--orange)"/>
      <rect x="0" y="0" width="8" height="290" fill="var(--red)"/>
      <rect x="0" y="290" width="8" height="290" fill="var(--orange)"/>
      <rect x="352" y="0" width="8" height="290" fill="var(--yellow)"/>
      <rect x="352" y="290" width="8" height="290" fill="var(--orange)"/>
    </g>
  </svg>
  <div class="brand"><span class="brand-dot"></span>Mabel's Home Daycare</div>
</section>

</body>
</html>
```